letterhead design for a investing company*

Design an appealing business letterhead to match with our existing logo and attract new customers. Our customers are mainly corporate managers which are detail oriented and judge the company ability to perform a good service based on small details. A professional letterhead will give a good first impression.

Target Market(s)

New customers and business owners

Industry/Entity Type

Marketplace

Font styles to use
Sans Serif
Script

Requirements
Must have
• Must be a professional and elegant design that attracts interest from people who receives it

```html
<!DOCTYPE html>
<html lang="en">
<head>
<meta charset="utf-8">
<title>Brightvest Letterhead</title>
<link href="https://fonts.googleapis.com/css2?family=Open+Sans:wght@400;600;700&family=Great+Vibes&display=swap" rel="stylesheet">
<style>
:root{
  --backdrop:#dccdb3;
  --paper:#ffffff;
  --gold:#f2b51b;
  --navy:#13203f;
  --ink:#2b2b2b;
  --muted:#4a4a4a;
  --ghost:#e6e7ea;
}
*{margin:0;padding:0;box-sizing:border-box}
html,body{width:1200px;height:898px;overflow:hidden;background:var(--backdrop)}
body{font-family:"Open Sans",Arial,sans-serif;color:var(--ink)}
.sheet{position:absolute;left:296px;top:19px;width:608px;height:860px;background:var(--paper);box-shadow:0 6px 22px rgba(0,0,0,.18);overflow:hidden}
.corner{position:absolute}
.corner--top{left:0;top:0}
.corner--bottom{right:0;bottom:0}
.brand{position:absolute;left:30px;top:84px;display:flex;align-items:center;gap:10px}
.brand__dot{width:34px;height:34px;border-radius:50%;background:var(--navy)}
.brand__name{font-size:30px;font-weight:700;color:var(--navy);letter-spacing:.2px}
.contact{position:absolute;right:22px;top:26px;display:flex;gap:8px}
.contact__lines{text-align:right;font-size:8px;line-height:11px;color:var(--ink)}
.contact__icons{display:flex;flex-direction:column;gap:9px}
.contact__icon{width:14px;height:14px;background:var(--gold);display:flex;align-items:center;justify-content:center}
.watermark{position:absolute;left:300px;top:150px;width:190px;height:400px;border-radius:90px 90px 60px 60px;background:linear-gradient(180deg,var(--ghost),#f1f2f4);opacity:.8}
.date{position:absolute;right:70px;top:250px;font-size:8px}
.recipient{position:absolute;left:82px;top:270px;font-size:7.5px;line-height:11px}
.recipient__name{font-weight:700;font-size:8.5px}
.recipient__role{font-size:6.5px}
.recipient b{display:inline-block;width:16px}
.letter{position:absolute;left:82px;top:360px;width:450px;font-size:7.8px;line-height:14px;color:var(--muted)}
.letter p{margin-bottom:20px}
.signoff{position:absolute;left:100px;top:620px}
.signoff__script{font-family:"Great Vibes",cursive;font-size:22px;color:var(--navy)}
.signoff__name{font-size:8px;font-weight:700;margin-top:2px}
.signoff__role{font-size:8px}
.footer-web{position:absolute;left:110px;top:770px;font-size:11px;letter-spacing:4px;color:var(--navy);font-weight:600}
</style>
</head>
<body>
<main class="sheet">
  <svg class="corner corner--top" width="260" height="190" viewBox="0 0 260 190" aria-hidden="true">
    <path d="M0 0 H250 Q70 30 0 180 Z" fill="var(--gold)"/>
    <path d="M0 150 Q60 40 220 6 Q90 48 12 160 Z" fill="var(--navy)"/>
    <path d="M0 0 H140 Q40 20 0 80 Z" fill="var(--gold)"/>
  </svg>

  <div class="brand">
    <span class="brand__dot"></span>
    <span class="brand__name">Brightvest</span>
  </div>

  <div class="contact">
    <div class="contact__lines">
      +000 55510 2040<br>+000 55510 2041<br>brightvest-example.com<br>hello@brightvest-example.com<br>12 Harbour Lane<br>Porto 4000
    </div>
    <div class="contact__icons">
      <span class="contact__icon"><svg width="8" height="8" viewBox="0 0 10 10"><path d="M2 1 L4 1 L5 3 L4 4 Q5 6 6 6 L7 5 L9 6 L9 8 Q5 9 1 3 Z" fill="#fff"/></svg></span>
      <span class="contact__icon"><svg width="8" height="8" viewBox="0 0 10 10"><rect x="1" y="2" width="8" height="6" fill="none" stroke="#fff"/><path d="M1 2 L5 5 L9 2" fill="none" stroke="#fff"/></svg></span>
      <span class="contact__icon"><svg width="8" height="8" viewBox="0 0 10 10"><path d="M5 9 Q1 5 1 4 A4 4 0 0 1 9 4 Q9 5 5 9 Z" fill="#fff"/><circle cx="5" cy="4" r="1.4" fill="var(--gold)"/></svg></span>
    </div>
  </div>

  <div class="watermark" role="img" aria-label="Faint brand mascot watermark"></div>

  <div class="date">Date, 10 September, 2019</div>

  <div class="recipient">
    <div class="recipient__name">Daniel Moreau</div>
    <div class="recipient__role">Chief Director</div>
    <div><b>A :</b>8 Quay Street, Lisbon - 1100</div>
    <div><b>W :</b>d.moreau@brightvest-example.com, www.brightvest-example.com</div>
    <div><b>P :</b>+000 - 55520 - 3090</div>
  </div>

  <section class="letter">
    <p>This is a sample letter that has been placed to demonstrate typing format (Your Company) letterhead design. When positioned properly, it will serve to work in harmony with all other elements letterhead. This letterhead design is meant to project an image.</p>
    <p>This letterhead design is meant to project an image of professionalism and reliability. By using simple alignment we have created a very spacious feeling. The simplicity suggests strength, the spaciousness contributes to the aesthetics of the layout. These basic qualities along with the (Your Company)</p>
    <p>look and help reinforce the (Your Company) brand. This letterhead design is meant to project an image of design. When positioned properly, it will serve to work in harmony with all the other elements of the letterhead, professionalism and reliability.</p>
    <p>This letterhead design is based on the (Form of your logo) from (Your Company) logo. Each stationery item we have created has a very spacious feeling. The simplicity suggests strength, the spaciousness contributes part of the (Form of your logo).</p>
  </section>

  <div class="signoff">
    <div class="signoff__script">Paul Harlan</div>
    <div class="signoff__name">Paul Harlan</div>
    <div class="signoff__role">Manager</div>
  </div>

  <div class="footer-web">www.brightvest-example.com</div>

  <svg class="corner corner--bottom" width="300" height="240" viewBox="0 0 300 240" aria-hidden="true">
    <path d="M300 0 V240 H20 Q230 190 300 0 Z" fill="var(--gold)"/>
    <path d="M300 70 Q250 200 110 236 Q260 215 300 110 Z" fill="var(--navy)"/>
    <path d="M300 130 V240 H170 Q270 210 300 130 Z" fill="var(--gold)"/>
  </svg>
</main>
</body>
</html>
```